Baby acupressure app for parents

We need an app for parents that teaches parents how to help them relieve their baby's imbalances (stomach ache, trouble sleeping etc.)

Please see the attached document (with info) and wireframes.

This project is urgent so please only participate if you're able to finish all screens within a few days after the contest is over.

Target Market(s)

Baby moms (20-40 years of age)

Industry/Entity Type

Baby Care

Colors
886aae
b768aa
e667a6
f68d4d
faa54b
fac994
f9ba93
f59195
fee18a

Requirements
Must have
• A high quality design that is both modern and very sleek and stylish.
Nice to have
• Simple animations to make the app "feel" like it's extreme high quality and make the user want to use it again and again
Should not have
• Sandwich menus

```html
<!DOCTYPE html>
<html lang="en">
<head>
<meta charset="utf-8">
<title>Rolig Pote – app screens</title>
<link rel="stylesheet" href="https://fonts.googleapis.com/css2?family=Montserrat:wght@400;500;600;700&display=swap">
<style>
  :root{
    --purple:#886aae;
    --purple-deep:#7a58a8;
    --button:#9a6fd2;
    --lilac:#c3aee6;
    --lilac-soft:#ddd0f0;
    --canvas:#ecebf0;
    --screen:#f6f5f8;
    --ink:#4a4458;
    --muted:#8d8798;
    --pink:#f9a9d9;
    --green:#c8f59a;
    --mint:#7eeacb;
    --cyan:#9ceaf2;
    --yellow:#fbea72;
    --dark:#3b3a40;
  }
  *{box-sizing:border-box;margin:0;padding:0}
  html,body{width:1200px;height:750px;overflow:hidden}
  body{background:var(--canvas);font-family:"Montserrat",sans-serif;color:var(--ink)}
  .board{display:grid;grid-template-columns:repeat(4,190px);grid-template-rows:repeat(2,340px);
    column-gap:80px;row-gap:30px;padding:20px 100px}
  .screen{position:relative;width:190px;height:340px;background:var(--screen);border-radius:6px;
    overflow:hidden;box-shadow:0 6px 18px rgba(80,60,110,.14);display:flex;flex-direction:column}
  .appbar{height:38px;background:var(--purple);color:#fff;display:flex;align-items:center;
    justify-content:center;position:relative;font-size:8px;font-weight:600;letter-spacing:1px;text-transform:uppercase;flex:none}
  .appbar .back{position:absolute;left:10px;top:13px}
  .appbar .restore{position:absolute;right:8px;top:8px;font-size:5px;letter-spacing:0;text-transform:none;text-align:center;font-weight:500}
  .content{flex:1;padding:10px;overflow:hidden;position:relative}
  .tabbar{height:40px;flex:none;display:flex;justify-content:space-around;align-items:center;border-top:1px solid #e6e3ec;background:#fff}
  .tab{display:flex;flex-direction:column;align-items:center;gap:2px;font-size:5.5px;color:var(--muted)}
  .tab.active{color:var(--purple)}
  .tab svg{width:10px;height:10px;stroke:currentColor;fill:none;stroke-width:1.6}
  .photo{border-radius:6px;background:linear-gradient(135deg,#f2d9c8,#d9c3b4 60%,#b9a7a0)}
  .body-text{font-size:6px;line-height:1.5;color:var(--muted);margin-top:8px}
  .btn{display:block;margin:10px auto 0;background:var(--button);color:#fff;border-radius:20px;
    font-size:7px;font-weight:600;padding:6px 18px;width:max-content}
  /* splash */
  .splash{background:linear-gradient(160deg,#b39bdc,#9a7fc9);color:#fff;align-items:center;justify-content:center;text-align:center}
  .splash.soft{background:linear-gradient(160deg,#c7b4e8,#b29ddd)}
  .brand{display:flex;align-items:center;gap:6px;font-size:11px;font-weight:600;letter-spacing:1px;text-transform:uppercase}
  .brand .dot{width:12px;height:12px;border-radius:50%;background:#fff}
  .splash .tagline{font-size:7.5px;margin-top:10px;opacity:.85}
  .splash .btn{margin-top:22px}
  .splash .legal{position:absolute;bottom:24px;left:22px;right:22px;font-size:5px;line-height:1.5;opacity:.7}
  /* imbalances */
  .list{padding:8px 0;display:flex;flex-direction:column;gap:6px}
  .row{display:flex;align-items:center;height:42px;border-radius:0 21px 21px 0;margin-right:8px}
  .row .thumb{width:40px;height:42px;flex:none;background:linear-gradient(135deg,#f1d6c6,#c9aa9b)}
  .row .txt{padding-left:8px}
  .row h3{font-size:7px;font-weight:700;text-transform:uppercase;color:#3a3545}
  .row p{font-size:5px;color:#555062;margin-top:2px}
  /* spots */
  .intro{font-size:6px;font-weight:600;line-height:1.4;color:var(--ink)}
  .spots{display:grid;grid-template-columns:1fr 1fr;gap:8px;margin-top:8px}
  .spot{background:#fff;border-radius:10px;height:66px;box-shadow:0 3px 10px rgba(120,90,170,.12);
    display:flex;flex-direction:column;align-items:center;justify-content:center;gap:6px;font-size:6.5px;color:var(--purple);font-weight:600}
  .spot .glyph{width:26px;height:26px;border-radius:50%;background:linear-gradient(135deg,var(--lilac),var(--button))}
  .advice{margin-top:10px;height:40px;border-radius:8px;background:linear-gradient(90deg,#fbd3ea,var(--pink));
    display:flex;justify-content:space-between;align-items:center;padding-left:8px;overflow:hidden}
  .advice small{font-size:5px;display:block;color:var(--ink)}
  .advice strong{font-size:9px;color:#e0409a;font-weight:600}
  .advice .portrait{width:34px;height:40px;background:linear-gradient(180deg,#e8c9c0,#c46a94)}
  /* upgrade */
  .card{background:#fff;border-radius:10px;box-shadow:0 3px 12px rgba(120,90,170,.12);padding:10px;text-align:center}
  .deal{display:flex;align-items:center;justify-content:space-between}
  .badge{width:44px;height:44px;border-radius:50%;border:2px solid var(--purple);display:flex;
    align-items:center;justify-content:center;font-size:9px;font-weight:700;color:var(--purple)}
  .price{text-align:right;color:var(--button)}
  .price small{font-size:6px;display:block}
  .price .timer{font-size:10px;font-weight:600}
  .price .amount{font-size:17px;font-weight:700}
  .ready{font-size:9px;font-weight:600;color:var(--button);margin-top:6px}
  .fine{font-size:5px;color:var(--muted);margin-top:3px;line-height:1.4}
  .bonus{margin-top:10px}
  .bonus h3{font-size:9px;font-weight:600;color:var(--ink)}
  .bonus p{font-size:6px;color:var(--button);margin-top:3px}
  .bonus .only{font-size:6px;color:var(--ink);text-align:right;margin-top:3px}
  .bonus .only b{font-size:9px;color:var(--button)}
  /* locked */
  .locked{background:var(--dark);color:#fff;text-align:center;padding:14px 12px;height:106px}
  .locked h3{font-size:8px;font-weight:600;margin-top:4px}
  .locked p{font-size:5px;opacity:.7;margin-top:3px}
  .locked .btn{margin-top:8px}
  .article h2{font-size:10px;font-weight:600;margin-top:8px}
</style>
</head>
<body>
<main class="board">

  <!-- welcome -->
  <section class="screen splash">
    <div class="brand"><span class="dot"></span>Rolig Pote</div>
    <p class="tagline">Help relieve your child's imbalances</p>
    <span class="btn">Lets get started</span>
    <p class="legal">Always consult a physician if you suspect your child is ill or in need of health care. See FAQ for more info.</p>
  </section>

  <!-- launch -->
  <section class="screen splash soft">
    <div class="brand"><span class="dot"></span>Rolig Pote</div>
  </section>

  <!-- home -->
  <section class="screen">
    <header class="appbar">Rolig Pote</header>
    <div class="content">
      <div class="photo" style="height:96px" role="img" aria-label="Photo of a smiling baby sitting with a pacifier"></div>
      <p class="body-text">Some intro text about the app, its content and a little text about the author. Some intro text about the app.</p>
      <p class="body-text">How to use the app and how the app works (preview some treatments and purchase others). Select "Imbalances" in the menu to get started.</p>
    </div>
    <nav class="tabbar">
      <span class="tab active"><svg viewBox="0 0 12 12"><path d="M2 6 6 2l4 4v4H2z"/></svg>Home</span>
      <span class="tab"><svg viewBox="0 0 12 12"><circle cx="6" cy="6" r="4.5"/><path d="M4 7.5q2 1.5 4 0"/></svg>Imbalances</span>
      <span class="tab"><svg viewBox="0 0 12 12"><circle cx="3" cy="6" r="1.3"/><circle cx="9" cy="3" r="1.3"/><circle cx="9" cy="9" r="1.3"/><path d="M4 5.4 8 3.6M4 6.6 8 8.4"/></svg>Share</span>
      <span class="tab"><svg viewBox="0 0 12 12"><circle cx="6" cy="6" r="4.5"/><path d="M6 5.5v3M6 3.5v.1"/></svg>About</span>
    </nav>
  </section>

  <!-- imbalances -->
  <section class="screen">
    <header class="appbar">Imbalances</header>
    <div class="content" style="padding:0">
      <div class="list">
        <div class="row" style="background:var(--green)"><div class="thumb" role="img" aria-label="Photo of a crying baby"></div><div class="txt"><h3>Colic</h3><p>Long and frequent crying is hard to deal with</p></div></div>
        <div class="row" style="background:var(--pink)"><div class="thumb" role="img" aria-label="Photo of a sleeping baby"></div><div class="txt"><h3>Growing pains</h3><p>Relieve pain that comes from growth spurts</p></div></div>
        <div class="row" style="background:var(--mint)"><div class="thumb" role="img" aria-label="Photo of a baby with a cold"></div><div class="txt"><h3>Cold, coughing etc.</h3><p>Winter time can be hard - help out your baby</p></div></div>
        <div class="row" style="background:var(--cyan)"><div class="thumb" role="img" aria-label="Photo of a toddler playing outside"></div><div class="txt"><h3>Ear pain</h3><p>Oh, those little ears can hurt so much</p></div></div>
        <div class="row" style="background:var(--yellow)"><div class="thumb" role="img" aria-label="Photo of a baby with eczema"></div><div class="txt"><h3>Eczema</h3><p>Soothe dry and irritated skin</p></div></div>
      </div>
    </div>
    <nav class="tabbar">
      <span class="tab"><svg viewBox="0 0 12 12"><path d="M2 6 6 2l4 4v4H2z"/></svg>Home</span>
      <span class="tab active"><svg viewBox="0 0 12 12"><circle cx="6" cy="6" r="4.5"/><path d="M4 7.5q2 1.5 4 0"/></svg>Imbalances</span>
      <span class="tab"><svg viewBox="0 0 12 12"><circle cx="3" cy="6" r="1.3"/><circle cx="9" cy="3" r="1.3"/><circle cx="9" cy="9" r="1.3"/><path d="M4 5.4 8 3.6M4 6.6 8 8.4"/></svg>Share</span>
      <span class="tab"><svg viewBox="0 0 12 12"><circle cx="6" cy="6" r="4.5"/><path d="M6 5.5v3M6 3.5v.1"/></svg>About</span>
    </nav>
  </section>

  <!-- ear pain detail -->
  <section class="screen">
    <header class="appbar"><svg class="back" width="12" height="10" viewBox="0 0 12 10" fill="none" stroke="#fff" stroke-width="1.4"><path d="M11 5H1M5 1 1 5l4 4"/></svg>Ear pain</header>
    <div class="content">
      <div class="photo" style="height:70px;background:linear-gradient(135deg,#f3dccd,#e6c3b0)" role="img" aria-label="Video still of a baby receiving a gentle massage"></div>
      <p class="body-text">This is some text about the specific imbalance. What could be the reasons for it, is it normal and what symptoms etc.</p>
      <div class="photo" style="height:62px;margin-top:8px;background:linear-gradient(135deg,#ece4e0,#cdbab2)" role="img" aria-label="Photo of a hand pressing a spot behind a baby's ear"></div>
      <p class="body-text">There are multiple ways to trigger some positive effects and you can try out multiple spots. Also check out the bonus.</p>
      <span class="btn" style="margin-top:6px">Start now</span>
    </div>
    <nav class="tabbar">
      <span class="tab"><svg viewBox="0 0 12 12"><path d="M2 6 6 2l4 4v4H2z"/></svg>Home</span>
      <span class="tab active"><svg viewBox="0 0 12 12"><circle cx="6" cy="6" r="4.5"/><path d="M4 7.5q2 1.5 4 0"/></svg>Imbalances</span>
      <span class="tab"><svg viewBox="0 0 12 12"><circle cx="3" cy="6" r="1.3"/><circle cx="9" cy="3" r="1.3"/><circle cx="9" cy="9" r="1.3"/><path d="M4 5.4 8 3.6M4 6.6 8 8.4"/></svg>Share</span>
      <span class="tab"><svg viewBox="0 0 12 12"><circle cx="6" cy="6" r="4.5"/><path d="M6 5.5v3M6 3.5v.1"/></svg>About</span>
    </nav>
  </section>

  <!-- ear pain spots -->
  <section class="screen">
    <header class="appbar"><svg class="back" width="12" height="10" viewBox="0 0 12 10" fill="none" stroke="#fff" stroke-width="1.4"><path d="M11 5H1M5 1 1 5l4 4"/></svg>Ear pain</header>
    <div class="content">
      <p class="intro">There are multiple ways to help relieve your child's ear pain. Select a spot to get started...</p>
      <div class="spots">
        <div class="spot"><span class="glyph" role="img" aria-label="Body icon"></span>Body</div>
        <div class="spot"><span class="glyph" role="img" aria-label="Face icon"></span>Face</div>
        <div class="spot"><span class="glyph" role="img" aria-label="Feet icon"></span>Feet</div>
        <div class="spot"><span class="glyph" role="img" aria-label="Hand icon"></span>Hand</div>
      </div>
      <div class="advice">
        <div><small>Get some additional advice from</small><strong>Mira Holm</strong><small>From a Danish acupressure book</small></div>
        <div class="portrait" role="img" aria-label="Portrait photo of the advisor"></div>
      </div>
    </div>
    <nav class="tabbar">
      <span class="tab"><svg viewBox="0 0 12 12"><path d="M2 6 6 2l4 4v4H2z"/></svg>Home</span>
      <span class="tab active"><svg viewBox="0 0 12 12"><circle cx="6" cy="6" r="4.5"/><path d="M4 7.5q2 1.5 4 0"/></svg>Imbalances</span>
      <span class="tab"><svg viewBox="0 0 12 12"><circle cx="3" cy="6" r="1.3"/><circle cx="9" cy="3" r="1.3"/><circle cx="9" cy="9" r="1.3"/><path d="M4 5.4 8 3.6M4 6.6 8 8.4"/></svg>Share</span>
      <span class="tab"><svg viewBox="0 0 12 12"><circle cx="6" cy="6" r="4.5"/><path d="M6 5.5v3M6 3.5v.1"/></svg>About</span>
    </nav>
  </section>

  <!-- locked post -->
  <section class="screen">
    <header class="appbar"><svg class="back" width="12" height="10" viewBox="0 0 12 10" fill="none" stroke="#fff" stroke-width="1.4"><path d="M11 5H1M5 1 1 5l4 4"/></svg>Ear pain</header>
    <div class="locked">
      <svg width="14" height="16" viewBox="0 0 14 16" fill="none" stroke="#fff" stroke-width="1.6"><rect x="1.5" y="7" width="11" height="8" rx="1.5"/><path d="M4 7V4.5a3 3 0 0 1 6 0V7"/></svg>
      <h3>This Post Locked</h3>
      <p>Simply unlock this post when you want to get all the details.</p>
      <span class="btn">Get full access!</span>
    </div>
    <div class="content article">
      <h2>Eustacic tubes</h2>
      <div class="photo" style="height:54px;margin-top:6px;background:linear-gradient(135deg,#e7dcf3,#c9b5e4)" role="img" aria-label="Photo of a baby having its ear gently pressed"></div>
      <p class="body-text">There are multiple ways to trigger some positive effects and you can try out multiple spots.</p>
    </div>
    <nav class="tabbar">
      <span class="tab"><svg viewBox="0 0 12 12"><path d="M2 6 6 2l4 4v4H2z"/></svg>Home</span>
      <span class="tab active"><svg viewBox="0 0 12 12"><circle cx="6" cy="6" r="4.5"/><path d="M4 7.5q2 1.5 4 0"/></svg>Imbalances</span>
      <span class="tab"><svg viewBox="0 0 12 12"><circle cx="3" cy="6" r="1.3"/><circle cx="9" cy="3" r="1.3"/><circle cx="9" cy="9" r="1.3"/><path d="M4 5.4 8 3.6M4 6.6 8 8.4"/></svg>Share</span>
      <span class="tab"><svg viewBox="0 0 12 12"><circle cx="6" cy="6" r="4.5"/><path d="M6 5.5v3M6 3.5v.1"/></svg>About</span>
    </nav>
  </section>

  <!-- upgrade -->
  <section class="screen">
    <header class="appbar"><svg class="back" width="12" height="10" viewBox="0 0 12 10" fill="none" stroke="#fff" stroke-width="1.4"><path d="M11 5H1M5 1 1 5l4 4"/></svg>Upgrade<span class="restore">↺<br>Restore purchase</span></header>
    <div class="content">
      <div class="card">
        <div class="deal">
          <div class="badge">15%</div>
          <div class="price"><small>Deal off</small><span class="timer">12:06:30</span><br><span class="amount">99 kr.</span></div>
        </div>
        <p class="ready">Ready for anything!</p>
        <p class="fine">All 12 imbalances, all future additions, all current &amp; upcoming videos</p>
        <span class="btn" style="margin-top:6px">Get full access!</span>
      </div>
      <div class="card bonus">
        <h3>Ear pain bonus</h3>
        <p>Unlock all spots for "Ear pain"</p>
        <div class="only">Just only <b>39 kr.</b></div>
      </div>
    </div>
    <nav class="tabbar">
      <span class="tab"><svg viewBox="0 0 12 12"><path d="M2 6 6 2l4 4v4H2z"/></svg>Home</span>
      <span class="tab active"><svg viewBox="0 0 12 12"><circle cx="6" cy="6" r="4.5"/><path d="M4 7.5q2 1.5 4 0"/></svg>Imbalances</span>
      <span class="tab"><svg viewBox="0 0 12 12"><circle cx="3" cy="6" r="1.3"/><circle cx="9" cy="3" r="1.3"/><circle cx="9" cy="9" r="1.3"/><path d="M4 5.4 8 3.6M4 6.6 8 8.4"/></svg>Share</span>
      <span class="tab"><svg viewBox="0 0 12 12"><circle cx="6" cy="6" r="4.5"/><path d="M6 5.5v3M6 3.5v.1"/></svg>About</span>
    </nav>
  </section>

</main>
</body>
</html>
```